Book Cover - For Best Selling Diet

Hi
Book cover required for a diet book being marketed to become a best seller
For best quality, image will be 2820 pixels on the shortest side and 4500 pixels on the longest side .
The book name : Bright Morning Plan
By Corinna Plett
( will add in the extra text once we see design - top and bottom subtitle )
I do not want a photo of a person on the book.
PLEASE SEE " THE 9 STEP FRAME" by Ned Galbury as an example of solid style and I also love Quiet Ledger for the font.
Branding Colours:
#F26432
#A4195C
#A7D8CC
Font that runs through our brand is : helvetica neue
This is for a book that will be marketed for #1 bestseller - So please only quality
designs that are designed in a unique style.
Thanks
Target Market(s)
Busy Working Mums, Affluent, 30+ .
Look and feel

```html
<!DOCTYPE html>
<html lang="en">
<head>
<meta charset="utf-8">
<title>Bright Morning Plan – Book Cover</title>
<link rel="stylesheet" href="https://fonts.googleapis.com/css2?family=Open+Sans:wght@700;800&family=Arimo:wght@400;700&display=swap">
<style>
  :root {
    --page-bg: #f2f2f2;
    --street-light: #c4c7cb;
    --street-mid: #7d848c;
    --street-dark: #4a4f55;
    --band-dark: #3a3a3c;
    --band-deep: #2b2b2d;
    --brand-orange: #F26432;
    --brand-berry: #A4195C;
    --brand-mint: #A7D8CC;
    --title-grey: #4a4a4a;
    --title-white: #f4f4f4;
    --title-shadow: #8a8a8a;
    --watch-face: #2a2a2e;
    --author-white: #ffffff;
  }
  * { margin: 0; padding: 0; box-sizing: border-box; }
  html, body {
    width: 900px;
    height: 1200px;
    overflow: hidden;
    background: var(--page-bg);
  }
  .book-cover {
    position: absolute;
    left: 130px;
    top: 60px;
    width: 640px;
    height: 1080px;
    overflow: hidden;
    background: var(--band-dark);
    box-shadow: 0 10px 30px rgba(0,0,0,0.25);
  }
  .city-scene {
    position: absolute;
    inset: 0 0 170px 0;
    background:
      linear-gradient(180deg, rgba(0,0,0,0) 0%, rgba(0,0,0,0) 60%, var(--street-dark) 82%, var(--band-dark) 100%),
      linear-gradient(90deg, var(--street-mid) 0%, var(--street-light) 30%, #d6d8db 50%, var(--street-light) 70%, var(--street-mid) 100%);
  }
  .bottom-band {
    position: absolute;
    left: 0; right: 0; bottom: 0;
    height: 220px;
    background: linear-gradient(180deg, rgba(58,58,60,0) 0%, var(--band-dark) 30%, var(--band-deep) 100%);
  }
  .title {
    position: absolute;
    left: 0; right: 0;
    top: 150px;
    text-align: center;
    font-family: "Open Sans", sans-serif;
    font-weight: 800;
    line-height: 1;
  }
  .title-lead {
    display: block;
    font-size: 60px;
    letter-spacing: -1.5px;
  }
  .title-lead .title-bright { color: var(--title-grey); }
  .title-lead .title-morning { color: var(--brand-orange); }
  .title-main {
    display: block;
    font-size: 250px;
    letter-spacing: -9px;
    color: var(--title-white);
    margin-top: -10px;
    text-shadow: 6px 6px 0 var(--title-shadow), 0 0 18px rgba(0,0,0,0.25);
  }
  .stopwatch {
    position: absolute;
    left: 150px;
    top: 560px;
    width: 340px;
    height: 340px;
  }
  .author {
    position: absolute;
    left: 0; right: 0;
    bottom: 66px;
    text-align: center;
    font-family: "Arimo", sans-serif;
    font-weight: 700;
    font-size: 42px;
    color: var(--author-white);
  }
</style>
</head>
<body>
  <main class="book-cover">
    <div class="city-scene" role="img" aria-label="Photograph of a busy city street with tall buildings, billboards, a pedestrian crossing and a delivery truck"></div>
    <div class="bottom-band"></div>

    <h1 class="title">
      <span class="title-lead"><span class="title-bright">Bright </span><span class="title-morning">Morning</span></span>
      <span class="title-main">Plan</span>
    </h1>

    <svg class="stopwatch" viewBox="0 0 340 340" role="img" aria-label="Illustration of a stopwatch set at fifteen minutes">
      <defs>
        <radialGradient id="watch-rim" cx="40%" cy="35%" r="70%">
          <stop offset="0%" stop-color="#F26432"/>
          <stop offset="100%" stop-color="#A4195C"/>
        </radialGradient>
      </defs>
      <circle cx="170" cy="175" r="160" fill="url(#watch-rim)"/>
      <circle cx="170" cy="175" r="128" fill="#2a2a2e"/>
    </svg>

    <p class="author">By Corinna Plett</p>
  </main>
</body>
</html>
```